Baby and kids clothes e-commerce website

We need a clothes ecommerce page with cart and live chat available in English and Spanish. Easy to maintain. Name of the shop is TULAVEN. I need it to be really soft colour palette and easy to navigate. It needs a mobile version.

LOGO NAME "TULAVEN" and there will be a very cute teddy next to it. Picture PELUMain will be the main Bear which could have different accessories such as picture attached PELUkids.

Target Market(s)

25-40 women with kids. Clothes will be quality baby and junior clothing.

Industry/Entity Type

Baby

Logo Text

TULAVEN

Coding

Coded - Design and coding required

Number of Pages Required

5+ page

Requirements
Must have
• It must have a cart, a live chat, account section and newsletter sign up.
• Option to add discounts and change different flash details like in brelvo.com. Also blog feature and all the social Access (including Pinterest). It also needs to have the option to add a product catalogue where products can be selected.
• It will be for baby and junior clothing.
• The 5 pages will be :
• MAIN
• BABY
• GIRLS
• BOYS
• OUTLET
• It needs to have the same pages in both English and Spanish.
Nice to have
• CART
• Account section
• Newsletter sign up
• Product catalogue section
• Discounts and vouchers
• Blog Access
• Social sites including pinterest

```html
<!DOCTYPE html>
<html lang="en">
<head>
<meta charset="utf-8">
<title>TULAVEN – Shop</title>
<link href="https://fonts.googleapis.com/css2?family=Open+Sans:wght@400;600;700&display=swap" rel="stylesheet">
<style>
:root{
  --blue:#2594d8;
  --ink:#333;
  --muted:#8a8a8a;
  --line:#e6e6e6;
  --banner:#9b9b9b;
  --foot:#3b3e43;
  --foot-deep:#2d2f33;
  --foot-text:#c9c9c9;
  --white:#fff;
}
*{box-sizing:border-box;margin:0;padding:0}
html,body{width:841px;height:1200px;overflow:hidden;background:var(--white)}
body{font-family:"Open Sans",Arial,sans-serif;color:var(--ink);font-size:11px;position:relative}
.topbar{height:26px;display:flex;justify-content:space-between;align-items:center;padding:0 76px;font-size:8px;color:var(--muted);border-bottom:1px solid var(--line)}
.topbar .social{display:flex;gap:9px}
.topbar .social span{width:7px;height:7px;border-radius:50%;background:#9a9a9a}
.header{height:96px;display:flex;align-items:center;justify-content:space-between;padding:0 76px}
.logo{font-weight:600;font-size:26px;color:var(--ink);letter-spacing:3px;line-height:1}
.nav{display:flex;align-items:center;gap:22px;font-size:9px;font-weight:600;color:#666}
.nav .active{color:var(--blue)}
.nav .btn{background:var(--blue);color:var(--white);padding:7px 14px;border-radius:14px}
.banner{height:26px;background:var(--banner);display:flex;align-items:center;justify-content:center;color:var(--white);font-size:8px}
.shop{padding:0 76px}
.toolbar{display:flex;gap:10px;align-items:center;margin:28px 0 22px}
.select{border:1px solid var(--line);height:20px;padding:0 8px;display:flex;align-items:center;justify-content:space-between;font-size:8px;color:#666;width:118px}
.view{width:20px;height:20px;border:1px solid var(--line);display:flex;align-items:center;justify-content:center}
.grid{display:grid;grid-template-columns:repeat(4,1fr);gap:22px 16px}
.card{border:1px solid var(--line);position:relative}
.photo{height:170px}
.badge{position:absolute;top:8px;left:8px;width:26px;height:26px;border-radius:50%;background:var(--blue);color:var(--white);font-size:8px;font-weight:700;display:flex;align-items:center;justify-content:center}
.info{padding:10px 10px 6px;height:56px}
.name{font-weight:700;font-size:10px;margin-bottom:5px}
.price-row{display:flex;justify-content:space-between;align-items:center}
.price{color:var(--blue);font-size:10px}
.price s{color:var(--muted);margin-right:4px}
.stars{color:var(--blue);font-size:9px;letter-spacing:1px}
.actions{border-top:1px solid var(--line);display:flex;justify-content:space-between;padding:6px 10px;font-size:7.5px;color:#666}
.footer{position:absolute;top:800px;left:0;width:841px;height:340px;background:var(--foot);color:var(--foot-text);padding:40px 76px;display:grid;grid-template-columns:1fr 1fr 1fr 1fr;gap:20px;font-size:8.5px;line-height:1.7}
.footer h4{color:var(--white);font-size:8.5px;font-weight:700;margin-bottom:14px;text-transform:uppercase}
.footer ul{list-style:none}
.footer li{margin-bottom:12px}
.footer li.current{color:var(--blue)}
.fsocial{display:flex;gap:9px;margin-top:16px}
.fsocial span{width:8px;height:8px;border-radius:50%;background:var(--foot-text)}
.plist li{display:flex;justify-content:space-between;align-items:center;margin-bottom:8px}
.plist b{color:var(--white);font-weight:600;display:block}
.plist .p{color:var(--blue)}
.plist .thumb{width:24px;height:24px}
.bottom{position:absolute;top:1140px;left:0;width:841px;height:60px;background:var(--foot-deep);color:var(--foot-text);font-size:8px;display:flex;align-items:center;justify-content:center}
</style>
</head>
<body>
<div class="topbar"><span>Call Us Today! 1800.555.0142 | hello@tulaven.com</span><div class="social"><span></span><span></span><span></span><span></span><span></span></div></div>
<header class="header">
  <div class="logo">TULAVEN</div>
  <nav class="nav"><span>HOME</span><span class="active">SHOP</span><span>BOYS</span><span>GIRLS</span><span>OUTLET</span><span class="btn">SHOP NOW</span></nav>
</header>
<div class="banner">Home / Shop Nav</div>
<main class="shop">
  <div class="toolbar">
    <div class="select">Sort by Default Order <span>⌄</span></div>
    <div class="select">Show 12 Products <span>⌄</span></div>
    <div class="view"><svg width="9" height="9"><rect x="0" y="0" width="4" height="4" fill="#888"/><rect x="5" y="0" width="4" height="4" fill="#888"/><rect x="0" y="5" width="4" height="4" fill="#888"/><rect x="5" y="5" width="4" height="4" fill="#888"/></svg></div>
    <div class="view"><svg width="9" height="9"><rect y="0" width="9" height="2" fill="#888"/><rect y="3.5" width="9" height="2" fill="#888"/><rect y="7" width="9" height="2" fill="#888"/></svg></div>
  </div>
  <div class="grid">
    <div class="card"><div class="photo" role="img" aria-label="White baby blouse" style="background:linear-gradient(#f7f7f7,#e9e9ec)"></div><span class="badge">Sale</span>
      <div class="info"><div class="name">Baby dress1</div><div class="price-row"><span class="price"><s>£350.00</s>£200.00</span><span class="stars">★★★★★</span></div></div>
      <div class="actions"><span>🛒 Add to cart</span><span>Details</span></div></div>
    <div class="card"><div class="photo" role="img" aria-label="Pink smocked baby dress" style="background:linear-gradient(#f6f1f1,#d98a8f)"></div>
      <div class="info"><div class="name">Baby dress2</div><div class="price-row"><span class="price">£170.00</span></div></div>
      <div class="actions"><span>🛒 Add to cart</span><span>Details</span></div></div>
    <div class="card"><div class="photo" role="img" aria-label="Light pink baby dress with white collar" style="background:linear-gradient(#f8f5f4,#e7b6b3)"></div>
      <div class="info"><div class="name">Baby dress3</div><div class="price-row"><span class="price">£55.00</span></div></div>
      <div class="actions"><span>🛒 Add to cart</span><span>Details</span></div></div>
    <div class="card"><div class="photo" role="img" aria-label="Toddler in pink dress sitting indoors" style="background:linear-gradient(#d9cbbd,#c99a8c)"></div>
      <div class="info"><div class="name">Baby dress4</div><div class="price-row"><span class="price">£150.00</span></div></div>
      <div class="actions"><span>🛒 Add to cart</span><span>Details</span></div></div>
    <div class="card"><div class="photo" role="img" aria-label="Child in blue classic jacket" style="background:linear-gradient(#dfe3e8,#8795a8)"></div>
      <div class="info"><div class="name">Blue Classic Jacket</div><div class="price-row"><span class="price">£150.00</span></div></div>
      <div class="actions"><span>🛒 Add to cart</span><span>Details</span></div></div>
    <div class="card"><div class="photo" role="img" aria-label="Little girl in lace tee and headband" style="background:linear-gradient(#c9b8a6,#a68d7b)"></div>
      <div class="info"><div class="name">Modern Love Tee</div><div class="price-row"><span class="price">£88.00</span></div></div>
      <div class="actions"><span>🛒 Add to cart</span><span>Details</span></div></div>
    <div class="card"><div class="photo" role="img" aria-label="Red plaid shirt" style="background:linear-gradient(#e8e2e2,#b4464a)"></div>
      <div class="info"><div class="name">Red Plaid Shirt</div><div class="price-row"><span class="price">£88.00</span></div></div>
      <div class="actions"><span>🛒 Add to cart</span><span>Details</span></div></div>
    <div class="card"><div class="photo" role="img" aria-label="Boy in cap playing outdoors on a path" style="background:linear-gradient(#b7c9a6,#8e9b86)"></div>
      <div class="info"><div class="name">Spring Printed Dress</div><div class="price-row"><span class="price">£47.00</span><span class="stars">★★★★★</span></div></div>
      <div class="actions"><span>🛒 Add to cart</span><span>Details</span></div></div>
  </div>
</main>
<footer class="footer">
  <div>
    <p>48 Willow Lane, Brookfield,<br>ST 20415<br>Phone: 1800.555.0142<br>Email: hello@tulaven.com<br>Web: www.tulaven.com</p>
    <div class="fsocial"><span></span><span></span><span></span><span></span><span></span><span></span></div>
  </div>
  <div><h4>Quick Links</h4><ul><li>› Home</li><li class="current">› Shop</li><li>› Boys</li><li>› Girls</li><li>› Outlet</li><li class="current">› Shop Now</li></ul></div>
  <div><h4>Product Categories</h4><ul><li>› Baby</li><li>› Boy</li><li>› Girl</li></ul></div>
  <div><h4>Products</h4><ul class="plist">
    <li><span><b>Baby dress1</b><span class="p">£150.00</span></span><span class="thumb" role="img" aria-label="Baby dress thumbnail" style="background:#e7b6b3"></span></li>
    <li><span><b>Baby dress2</b><span class="p">£100.00</span></span><span class="thumb" role="img" aria-label="Baby dress thumbnail" style="background:#f1f1f1"></span></li>
    <li><span><b>Baby dress3</b><span class="p"><s>£350.00</s> £200.00</span></span><span class="thumb" role="img" aria-label="Baby dress thumbnail" style="background:#d98a8f"></span></li>
    <li><span><b>Baby dress4</b><span class="p">£47.00</span></span><span class="thumb" role="img" aria-label="Baby dress thumbnail" style="background:#f3e0df"></span></li>
    <li><span><b>Modern Love Tee</b><span class="p">£88.00</span></span><span class="thumb" role="img" aria-label="Tee thumbnail" style="background:#c9b8a6"></span></li>
  </ul></div>
</footer>
<div class="bottom">© Copyright 2017 | TULAVEN | All Rights Reserved</div>
</body>
</html>
```